Pemberton Dialworks Business Card Design

Double Sided Business Card Design for a Locksmith company specializing in Safecracking, safe & vault service.

```html
<!DOCTYPE html>
<html lang="en">
<head>
<meta charset="utf-8">
<title>Pemberton Dialworks – Business Card</title>
<link href="https://fonts.googleapis.com/css2?family=Lato:wght@400;900&display=swap" rel="stylesheet">
<style>
  :root {
    --backdrop: #2b2c2e;
    --card: #0a0c0d;
    --green: #2a8a45;
    --green-faint: #16301f;
    --white: #ffffff;
    --grey-text: #e6e6e6;
  }
  html, body {
    margin: 0;
    padding: 0;
    width: 1200px;
    height: 970px;
    overflow: hidden;
    background: var(--backdrop);
    font-family: "Lato", sans-serif;
  }
  .canvas {
    position: relative;
    width: 1200px;
    height: 970px;
  }
  .card {
    position: absolute;
    left: 250px;
    width: 700px;
    height: 400px;
    background: var(--card);
    overflow: hidden;
    box-shadow: 0 10px 30px rgba(0,0,0,0.45);
  }
  .card::after {
    content: "";
    position: absolute;
    left: 0; right: 0; bottom: 0;
    height: 6px;
    background: var(--green);
  }
  .card-front { top: 60px; }
  .card-back { top: 510px; }

  .brand {
    display: flex;
    align-items: center;
    gap: 18px;
  }
  .brand-dot {
    width: 64px;
    height: 64px;
    border-radius: 50%;
    background: var(--green);
    flex: none;
  }
  .brand-name {
    font-weight: 900;
    color: var(--white);
    text-transform: uppercase;
    line-height: 1.02;
    letter-spacing: 1px;
    font-size: 34px;
  }
  .card-front .brand {
    position: absolute;
    left: 50%;
    top: 50%;
    transform: translate(-50%, -58%);
  }
  .card-back .brand {
    position: absolute;
    left: 60px;
    top: 150px;
    gap: 14px;
  }
  .card-back .brand-dot { width: 50px; height: 50px; }
  .card-back .brand-name { font-size: 26px; }

  .divider {
    position: absolute;
    left: 330px;
    top: 90px;
    width: 2px;
    height: 200px;
    background: var(--green);
  }
  .decor-circle {
    position: absolute;
    right: -70px;
    bottom: -90px;
    width: 300px;
    height: 300px;
    border-radius: 50%;
    background: var(--green-faint);
  }
  .contact {
    position: absolute;
    left: 370px;
    top: 70px;
    color: var(--grey-text);
  }
  .contact-name {
    margin: 0;
    font-weight: 900;
    font-size: 30px;
    color: var(--green);
    text-transform: uppercase;
    letter-spacing: 0.5px;
  }
  .contact-role {
    margin: 2px 0 18px;
    font-size: 17px;
  }
  .contact-address {
    margin: 0 0 14px;
    font-style: normal;
    font-size: 17px;
    line-height: 1.3;
  }
  .contact-list {
    list-style: none;
    margin: 0;
    padding: 0;
    font-size: 17px;
  }
  .contact-list li {
    display: flex;
    align-items: center;
    gap: 12px;
    height: 28px;
  }
  .contact-icon {
    width: 18px;
    height: 18px;
    flex: none;
  }
</style>
</head>
<body>
<main class="canvas">

  <section class="card card-front" aria-label="Card front">
    <div class="brand">
      <span class="brand-dot"></span>
      <span class="brand-name">Pemberton<br>Dialworks</span>
    </div>
  </section>

  <section class="card card-back" aria-label="Card back">
    <div class="decor-circle"></div>

    <div class="brand">
      <span class="brand-dot"></span>
      <span class="brand-name">Pemberton<br>Dialworks</span>
    </div>

    <div class="divider"></div>

    <div class="contact">
      <h2 class="contact-name">Morgan Hale</h2>
      <p class="contact-role">Founder &amp; CEO</p>
      <address class="contact-address">
        1234 First Line Address<br>
        5678 Second Line Address
      </address>
      <ul class="contact-list">
        <li>
          <svg class="contact-icon" viewBox="0 0 24 24" fill="none" stroke="#2a8a45" stroke-width="2.4" stroke-linecap="round" stroke-linejoin="round"><path d="M5 3h4l2 5-3 2a11 11 0 0 0 6 6l2-3 5 2v4a2 2 0 0 1-2 2A17 17 0 0 1 3 5a2 2 0 0 1 2-2z"/></svg>
          <span>1234567890</span>
        </li>
        <li>
          <svg class="contact-icon" viewBox="0 0 24 24" fill="none" stroke="#2a8a45" stroke-width="2.4" stroke-linejoin="round"><rect x="2" y="5" width="20" height="14"/><path d="M2 5l10 8 10-8"/></svg>
          <span>info@yourmail.com</span>
        </li>
        <li>
          <svg class="contact-icon" viewBox="0 0 24 24" fill="none" stroke="#2a8a45" stroke-width="2"><circle cx="12" cy="12" r="10"/><path d="M2 12h20M12 2c3 3 3 17 0 20M12 2c-3 3-3 17 0 20"/></svg>
          <span>www.yourwebsite.com</span>
        </li>
      </ul>
    </div>
  </section>

</main>
</body>
</html>
```